Business card

creative business card for newly created national firm that specializes in high-density storage for retail markets. Looking for creativity and overall theme that will differentiate from others in this unique niche ...essentially a design that will provide instant recognition as we develop our identity in the marketplace. possible initial thoughts are attached with logo separately

Retail

```html
<!DOCTYPE html>
<html lang="en">
<head>
<meta charset="utf-8">
<title>Stackwise Storage Group – Business Card Concepts</title>
<link rel="stylesheet" href="https://fonts.googleapis.com/css2?family=Open+Sans:wght@400;700&family=Tinos:wght@400;700&family=Arimo:wght@400;700&display=swap">
<style>
  :root {
    --sky: #4bb9ea;
    --ink: #1d4e6b;
    --navy: #15324a;
    --band: #2a80a5;
    --grey: #8a8a8a;
    --paper: #ffffff;
    --shadow: rgba(0,0,0,0.35);
  }
  * { margin: 0; padding: 0; box-sizing: border-box; }
  html, body { width: 1200px; height: 900px; overflow: hidden; background: var(--paper); }
  .sheet { position: relative; width: 1200px; height: 900px; }

  .card {
    position: absolute;
    background: var(--paper);
    box-shadow: 8px 10px 12px var(--shadow);
    overflow: hidden;
  }
  .card--r1-front { left: 96px; top: 25px; width: 474px; height: 258px; }
  .card--r1-back  { left: 615px; top: 25px; width: 470px; height: 258px; }
  .card--r2-front { left: 96px; top: 340px; width: 474px; height: 255px; }
  .card--r2-back  { left: 605px; top: 340px; width: 470px; height: 255px; }
  .card--r3-front { left: 96px; top: 640px; width: 474px; height: 260px; box-shadow: 8px 0 12px var(--shadow); }
  .card--r3-back  { left: 600px; top: 640px; width: 475px; height: 255px; }

  .abs { position: absolute; white-space: nowrap; }

  /* wordmark */
  .wordmark {
    position: absolute;
    display: flex;
    align-items: center;
    gap: 8px;
  }
  .wordmark__name {
    font-family: "Open Sans", sans-serif;
    font-weight: 400;
    color: var(--ink);
    line-height: 0.98;
    letter-spacing: 0.5px;
  }
  .wordmark__square { background: var(--sky); flex: none; }

  .serif { font-family: "Tinos", serif; }
  .sans  { font-family: "Arimo", sans-serif; }

  /* row 1 */
  .r1-wordmark { left: 11px; top: 6px; }
  .r1-wordmark .wordmark__name { font-size: 26px; }
  .r1-wordmark .wordmark__square { width: 34px; height: 34px; }
  .r1-name { left: 0; width: 478px; top: 113px; text-align: center; font-family: "Open Sans", sans-serif; font-weight: 700; font-size: 22px; color: var(--sky); }
  .r1-phone { left: 0; width: 478px; top: 145px; text-align: center; font-family: "Open Sans", sans-serif; font-size: 17px; color: var(--ink); }
  .r1-tag { left: 0; width: 478px; top: 172px; text-align: center; font-size: 13px; color: var(--ink); }
  .r1-web { left: 0; width: 474px; top: 227px; text-align: center; font-size: 11px; color: var(--ink); }

  .r1-addr { left: 22px; top: 163px; font-size: 11px; line-height: 14px; color: var(--ink); }
  .r1-addr p + p { margin-top: 13px; }
  .r1-divider { left: 196px; top: 162px; width: 3px; height: 66px; background: var(--ink); }
  .r1-online { left: 276px; top: 192px; font-size: 11px; line-height: 20px; color: var(--ink); }

  /* row 2 */
  .r2-wordmark { left: 19px; top: 82px; }
  .r2-wordmark .wordmark__name { font-size: 26px; }
  .r2-wordmark .wordmark__square { width: 36px; height: 36px; }
  .r2-divider { left: 218px; top: 80px; width: 4px; height: 81px; background: var(--sky); }
  .r2-name { left: 251px; top: 68px; font-weight: 700; font-size: 22px; color: var(--grey); letter-spacing: 0.5px; }
  .r2-phone { left: 251px; top: 94px; font-size: 14px; color: var(--ink); }
  .r2-tag { left: 251px; top: 123px; font-size: 13px; color: var(--ink); }
  .r2-web { left: 251px; top: 152px; font-size: 14px; color: var(--ink); }

  .r2-back { left: 15px; top: 96px; font-weight: 700; font-size: 11px; line-height: 13px; color: var(--navy); }
  .r2-rule { height: 1px; background: var(--navy); margin: 7px 0 14px; }
  .r2-rule--short { width: 99px; }
  .r2-rule--long { width: 160px; margin-bottom: 16px; }
  .r2-online { line-height: 20px; }

  /* row 3 */
  .r3-wordmark { left: 0; width: 474px; top: 14px; justify-content: center; }
  .r3-wordmark .wordmark__name { font-size: 26px; }
  .r3-wordmark .wordmark__square { width: 36px; height: 36px; }
  .r3-band { left: 0; top: 147px; width: 474px; height: 45px; background: var(--band); }
  .r3-name { left: 0; width: 474px; top: 150px; text-align: center; font-family: "Open Sans", sans-serif; font-weight: 700; font-size: 16px; color: #fff; }
  .r3-phone { left: 0; width: 474px; top: 172px; text-align: center; font-size: 14px; color: #6d7a82; }
  .r3-tag { left: 0; width: 474px; top: 197px; text-align: center; font-family: "Open Sans", sans-serif; font-size: 11px; color: var(--band); }
  .r3-web { left: 0; width: 474px; top: 236px; text-align: center; font-family: "Open Sans", sans-serif; font-size: 13px; color: var(--band); }

  .r3-back-band { left: 0; top: 80px; width: 475px; height: 81px; background: var(--band); }
  .r3-col { top: 108px; font-weight: 700; font-size: 10.5px; line-height: 12px; color: var(--navy); }
  .r3-col--po { left: 6px; }
  .r3-col--street { left: 119px; }
  .r3-col--online { left: 286px; }
</style>
</head>
<body>
<main class="sheet">

  <!-- Concept 1 front -->
  <section class="card card--r1-front">
    <div class="wordmark r1-wordmark">
      <div class="wordmark__name">STACKWISE<br>STORAGE<br>GROUP</div>
      <div class="wordmark__square"></div>
    </div>
    <h2 class="abs r1-name">DANA MORROW</h2>
    <p class="abs r1-phone">855-STACK-HIGH</p>
    <p class="abs serif r1-tag">Maximize Your Space</p>
    <p class="abs serif r1-web">www.stackwisestorage.com</p>
  </section>

  <!-- Concept 1 back -->
  <section class="card card--r1-back">
    <div class="abs serif r1-addr">
      <p>PO Box Number<br>Pine Hill, AZ 99999</p>
      <p>Mesa Vista Street Address<br>Pine Hill, AZ 88888</p>
    </div>
    <div class="abs r1-divider"></div>
    <div class="abs serif r1-online">
      <p>www.stackwisestorage.com</p>
      <p>hello@stackwisestorage.com</p>
    </div>
  </section>

  <!-- Concept 2 front -->
  <section class="card card--r2-front">
    <div class="wordmark r2-wordmark">
      <div class="wordmark__name">STACKWISE<br>STORAGE<br>GROUP</div>
      <div class="wordmark__square"></div>
    </div>
    <div class="abs r2-divider"></div>
    <h2 class="abs serif r2-name">DANA MORROW</h2>
    <p class="abs serif r2-phone">855-STACK-HIGH</p>
    <p class="abs serif r2-tag">Maximize Your Space</p>
    <p class="abs sans r2-web">www.stackwisestorage.com</p>
  </section>

  <!-- Concept 2 back -->
  <section class="card card--r2-back">
    <div class="abs sans r2-back">
      <p>PO Box Number<br>Pine Hill, AZ 99999</p>
      <div class="r2-rule r2-rule--short"></div>
      <p>Mesa Vista Street Address<br>Pine Hill, AZ 88888</p>
      <div class="r2-rule r2-rule--long"></div>
      <div class="r2-online">
        <p>www.stackwisestorage.com</p>
        <p>hello@stackwisestorage.com</p>
      </div>
    </div>
  </section>

  <!-- Concept 3 front -->
  <section class="card card--r3-front">
    <div class="wordmark r3-wordmark">
      <div class="wordmark__name">STACKWISE<br>STORAGE<br>GROUP</div>
      <div class="wordmark__square"></div>
    </div>
    <div class="abs r3-band"></div>
    <h2 class="abs r3-name">DANA MORROW</h2>
    <p class="abs serif r3-phone">855-STACK-HIGH</p>
    <p class="abs r3-tag">Maximize Your Space</p>
    <p class="abs r3-web">www.stackwisestorage.com</p>
  </section>

  <!-- Concept 3 back -->
  <section class="card card--r3-back">
    <div class="abs r3-back-band"></div>
    <p class="abs sans r3-col r3-col--po">PO Box Number<br>Pine Hill, AZ 99999</p>
    <p class="abs sans r3-col r3-col--street">Mesa Vista Street Address<br>Pine Hill, AZ 88888</p>
    <p class="abs sans r3-col r3-col--online">www.stackwisestorage.com<br>hello@stackwisestorage.com</p>
  </section>

</main>
</body>
</html>
```